Tri-fold Brochure Design for Banking Business

The brochure we have needs to be improved - more business like and more attractive. Logo file and brochure is attached. I would like to be able to edit the text after you get done. Your ideas and changes to text are welcome. See our website www.quillbrookadvisory.com for our theme. We can use indesign to edit the text after you complete. However, please make changes to the text we have in the design that it uploaded. Your comments and changes are welcome.

Target Market(s)

Human Resources and learning & development staff at the global investment banks - Fenwright Carrow, QTRV, etc.

Industry/Entity Type

Investment Banking

Logo Text

Quillbrook Advisory Group

Font styles to use
Serif
Sans Serif

Colors
33a6d7
0493ce
3277b5
fbf289
fdf9cf
fbee3e
0555a3
85acd3

Requirements
Must have
• Must be similar to our website www.quillbrookadvisory.com. Needs to be business-like, clean fonts, sharp design. Our logo - of course.
Nice to have
• City images - seems to be our theme.

```html
<!DOCTYPE html>
<html lang="en">
<head>
<meta charset="utf-8">
<title>Quillbrook Advisory Group – Tri-fold Brochure</title>
<link href="https://fonts.googleapis.com/css2?family=Oswald:wght@500;600&family=Roboto:ital,wght@0,400;1,400;1,700&display=swap" rel="stylesheet">
<style>
  :root{
    --yellow:#fbd914;
    --yellow-soft:#fbee3e;
    --navy:#0a4a94;
    --blue:#0555a3;
    --blue-mid:#2565b8;
    --blue-bright:#3277b5;
    --sky-top:#f4f8fc;
    --sky-low:#a9c6e6;
    --ink:#0d0d12;
    --white:#ffffff;
  }
  *{box-sizing:border-box;margin:0;padding:0}
  html,body{width:1200px;height:762px;overflow:hidden;background:#d9d9d9}
  .brochure{position:relative;width:1200px;height:762px;overflow:hidden;font-family:"Roboto",Arial,sans-serif}
  .shapes{position:absolute;inset:0}
  .ribbon{position:absolute;font-family:"Oswald","Arial Narrow",sans-serif;font-weight:600;font-style:italic;font-size:26px;line-height:1;padding:10px 50px 10px 26px;clip-path:polygon(0 0,100% 0,88% 50%,100% 100%,0 100%)}
  .ribbon--about{left:10px;top:22px;background:var(--navy);color:var(--yellow)}
  .ribbon--contact{left:420px;top:40px;background:var(--yellow);color:var(--navy)}
  .about-copy{position:absolute;left:40px;top:88px;width:330px;color:var(--blue);font-style:italic;font-size:14.5px;line-height:1.2}
  .about-copy p{margin-bottom:12px}
  .envelope{position:absolute;left:720px;top:52px}
  .contacts{position:absolute;left:430px;top:102px;width:360px}
  .contact{margin-bottom:8px}
  .contact__region{display:block;color:var(--yellow);font-weight:700;font-style:italic;font-size:15px}
  .contact__mail{display:block;color:var(--white);font-size:15px}
  .tagline{position:absolute;left:440px;top:400px;color:var(--white);font-family:"Oswald","Arial Narrow",sans-serif;font-weight:500;font-style:italic;font-size:27px;line-height:1.02}
  .brand{position:absolute;left:870px;top:46px;display:flex;align-items:center;gap:10px;font-family:"Oswald","Arial Narrow",sans-serif;font-weight:600;font-size:26px;color:var(--ink)}
  .brand__mark{width:26px;height:26px;background:var(--blue-bright)}
  .headline{position:absolute;right:34px;top:176px;text-align:right;font-family:"Oswald","Arial Narrow",sans-serif;font-weight:600;font-size:50px;line-height:1.08;color:var(--blue-mid);text-transform:uppercase}
  .headline .dark{color:var(--ink)}
  .web{position:absolute;color:var(--white);font-size:16px;font-weight:400}
  .web--left{left:70px;top:712px}
  .web--mid{left:450px;top:712px}
  .web--right{left:870px;top:712px}
</style>
</head>
<body>
<main class="brochure">
  <svg class="shapes" width="1200" height="762" viewBox="0 0 1200 762">
    <defs>
      <linearGradient id="sky" x1="0" y1="0" x2="0" y2="1">
        <stop offset="0" stop-color="#f4f8fc"/>
        <stop offset="1" stop-color="#a9c6e6"/>
      </linearGradient>
      <linearGradient id="london" x1="0" y1="0" x2="0" y2="1">
        <stop offset="0" stop-color="#d9b27a"/>
        <stop offset="0.45" stop-color="#6a6f78"/>
        <stop offset="1" stop-color="#253444"/>
      </linearGradient>
      <linearGradient id="harbour" x1="0" y1="0" x2="0" y2="1">
        <stop offset="0" stop-color="#b6c9dc"/>
        <stop offset="0.55" stop-color="#7b8794"/>
        <stop offset="1" stop-color="#3d5670"/>
      </linearGradient>
      <linearGradient id="bandFade" x1="0" y1="0" x2="0" y2="1">
        <stop offset="0" stop-color="#0555a3" stop-opacity="0"/>
        <stop offset="1" stop-color="#0555a3" stop-opacity="0.95"/>
      </linearGradient>
    </defs>
    <!-- left panel -->
    <rect class="panel-about" x="0" y="0" width="400" height="762" fill="var(--yellow)"/>
    <polygon fill="#d9b60f" points="0,250 400,330 400,370 0,290"/>
    <polygon role="img" aria-label="City riverside skyline at dusk" fill="url(#london)" points="0,270 400,350 400,762 0,762"/>
    <!-- middle panel -->
    <rect x="400" y="0" width="400" height="762" fill="var(--navy)"/>
    <rect role="img" aria-label="World map silhouette" x="440" y="300" width="180" height="95" rx="6" fill="#ffffff" opacity="0.85"/>
    <rect role="img" aria-label="Harbour city skyline" x="400" y="470" width="400" height="230" fill="url(#harbour)"/>
    <rect x="400" y="470" width="400" height="90" fill="url(#bandFade)" transform="rotate(180 600 515)"/>
    <!-- right panel -->
    <rect x="800" y="0" width="400" height="762" fill="url(#sky)"/>
    <rect role="img" aria-label="Harbour city skyline with mountains" x="800" y="420" width="400" height="300" fill="url(#harbour)"/>
    <!-- delta shapes -->
    <polygon fill="var(--blue-mid)" points="800,225 400,700 400,762 1200,762 1200,700"/>
    <polygon fill="var(--yellow-soft)" points="800,225 430,680 470,680 805,320 1000,690 1060,690"/>
    <polygon fill="var(--blue-bright)" points="805,320 470,680 1000,690"/>
    <polygon role="img" aria-label="Harbour skyline with tall tower" fill="url(#harbour)" points="800,360 560,660 975,665"/>
    <rect x="400" y="695" width="800" height="67" fill="var(--blue)"/>
    <rect x="0" y="695" width="400" height="67" fill="#1c2a38" opacity="0.5"/>
  </svg>

  <div class="ribbon ribbon--about">ABOUT US</div>
  <div class="about-copy">
    <p>Quillbrook Advisory Group efficiently provides complete sales, marketing and logistical support for all our programs, no matter the location.</p>
    <p>Our globally located trainers have extensive experience, both as industry professionals and as trainers.</p>
    <p>Our highly qualified logistical team complement the training services, providing reliable and efficient support.</p>
  </div>

  <div class="ribbon ribbon--contact">GET IN TOUCH</div>
  <svg class="envelope" width="38" height="26" viewBox="0 0 38 26" aria-hidden="true">
    <rect x="1" y="1" width="36" height="24" fill="#fff"/>
    <polyline points="1,1 19,15 37,1" fill="none" stroke="#0a4a94" stroke-width="2"/>
  </svg>
  <div class="contacts">
    <div class="contact"><span class="contact__region">GLOBAL:</span><span class="contact__mail">elena.varro@quillbrookadvisory.com</span></div>
    <div class="contact"><span class="contact__region">ASIA:</span><span class="contact__mail">owen.pritch@quillbrookadvisory.com</span></div>
    <div class="contact"><span class="contact__region">UNITED STATES:</span><span class="contact__mail">leo.farrant@quillbrookadvisory.com</span></div>
    <div class="contact"><span class="contact__region">EUROPE:</span><span class="contact__mail">neil.ashcombe@quillbrookadvisory.com</span></div>
  </div>
  <div class="tagline">WORLDWIDE<br>TRAINING<br>SERVICE</div>

  <div class="brand"><span class="brand__mark"></span>Quillbrook Advisory Group</div>
  <h1 class="headline"><span class="dark">Your</span> Expert<br>Training<br><span class="dark">And</span> Consulting<br>Partner</h1>

  <span class="web web--left">www.quillbrookadvisory.com</span>
  <span class="web web--mid">www.quillbrookadvisory.com</span>
  <span class="web web--right">www.quillbrookadvisory.com</span>
</main>
</body>
</html>
```